BQL Groundworks & Freight Business Card

Can you please design a business card for an Earthworks, Haulage truck and machinery hire company. They also provide sand soil and mulch supply, as well as screening of products. Can you re-create the logo from the attached but add BQL Groundworks & Freight just use the three diamond design.

Target Market(s)

Earthmoving and Transport, Landscapers, Construction

Contact Information for Business Card

ABN 52 907 334 816, Doug Pelham, Managing Director, BQL Groundworks & Freight Mobile 0438 256 904 Email bqlfreight2010@mailvane.net

Font styles to use
Sans Serif

Colors
ec1f27
000000
cbcbcb
ffffff

Requirements
Must have
• Listed on the back, Earthworks | Haulage | Truck and Machinery Hire | Sand, Soil & Mulch Supply | Screening of Products
Nice to have
• Would be good for it to look appealing to a mans man, because it relates to heavy machinery, earthworks, construction etc. Black, red and white would be good maybe with a bit of silver somewhere.
Should not have
• not sure

```html
<!DOCTYPE html>
<html lang="en">
<head>
<meta charset="utf-8">
<title>BQL Groundworks &amp; Freight – Business Card</title>
<link rel="stylesheet" href="https://fonts.googleapis.com/css2?family=Lato:wght@400;700;900&family=Open+Sans:wght@400&family=Tinos&display=swap">
<style>
  :root {
    --brand-red: #ec1f27;
    --ink: #000000;
    --card-black: #0b0b0b;
    --silver: #cbcbcb;
    --paper: #ffffff;
    --backdrop: #e4e4e4;
  }
  * { box-sizing: border-box; margin: 0; padding: 0; }
  html, body {
    width: 1200px;
    height: 1200px;
    overflow: hidden;
    background: var(--backdrop);
  }
  .canvas {
    position: relative;
    width: 1200px;
    height: 1200px;
  }
  .card {
    position: absolute;
    width: 839px;
    height: 479px;
    box-shadow: 0 6px 18px rgba(0,0,0,0.25);
  }
  .card--front { left: 108px; top: 78px; background: var(--paper); color: var(--ink); }
  .card--back  { left: 245px; top: 604px; background: var(--card-black); color: var(--paper); }

  .brand-mark {
    position: absolute;
    display: flex;
    align-items: center;
    gap: 18px;
    font-family: "Lato", sans-serif;
    font-weight: 900;
    color: var(--brand-red);
    letter-spacing: 6px;
  }
  .brand-mark__square {
    display: block;
    background: var(--brand-red);
  }
  .card--front .brand-mark { left: 70px; top: 118px; font-size: 92px; line-height: 1; }
  .card--front .brand-mark__square { width: 34px; height: 34px; }

  .services {
    position: absolute;
    left: 10px;
    top: 308px;
    width: 410px;
    text-align: center;
    font-family: "Open Sans", sans-serif;
    font-size: 15px;
    line-height: 1.45;
  }
  .divider {
    position: absolute;
    left: 434px;
    top: 68px;
    width: 4px;
    height: 342px;
    background: var(--ink);
  }
  .person { position: absolute; left: 515px; top: 62px; }
  .person__name {
    font-family: "Open Sans", sans-serif;
    font-size: 43px;
    font-weight: 400;
    line-height: 1.1;
  }
  .person__title {
    font-family: "Open Sans", sans-serif;
    font-size: 16px;
    text-align: right;
    margin-top: -4px;
    padding-right: 20px;
  }
  .contact {
    position: absolute;
    left: 462px;
    top: 198px;
    font-family: "Open Sans", sans-serif;
    font-size: 26px;
    line-height: 1.35;
  }
  .contact__label { display: inline-block; width: 120px; }
  .address {
    position: absolute;
    right: 42px;
    top: 340px;
    text-align: right;
    font-family: "Tinos", serif;
    font-size: 26px;
    line-height: 1.35;
  }

  .card--back .brand-mark {
    left: 0; right: 0; top: 140px;
    justify-content: center;
    font-size: 120px;
    line-height: 1;
  }
  .card--back .brand-mark__square { width: 44px; height: 44px; }
  .company-name {
    position: absolute;
    left: 0; right: 0;
    top: 330px;
    text-align: center;
    font-family: "Lato", sans-serif;
    font-size: 30px;
    font-weight: 400;
    color: var(--paper);
  }
</style>
</head>
<body>
<main class="canvas">
  <section class="card card--front" aria-label="Business card front">
    <div class="brand-mark"><span class="brand-mark__square"></span>BQL</div>
    <p class="services">Earthworks | Haulage | Truck and Machinery Hire<br>Sand, Soil &amp; Mulch Supply | Screening of Products</p>
    <div class="divider"></div>
    <div class="person">
      <h1 class="person__name">Doug Pelham</h1>
      <p class="person__title">Managing Director</p>
    </div>
    <p class="contact">
      <span class="contact__label">Mobile</span>0438 256 904<br>
      bqlfreight2010@mailvane.net
    </p>
    <p class="address">42 Barrow Crest<br>Kelvale 6031<br>Perth, WA.</p>
  </section>

  <section class="card card--back" aria-label="Business card back">
    <div class="brand-mark"><span class="brand-mark__square"></span>BQL</div>
    <p class="company-name">BQL Groundworks &amp; Freight</p>
  </section>
</main>
</body>
</html>
```